Classic Minimalistic Business Card

Design a classic, minimalistic Business Card. Please find inspiration in the attached Classic Minimalistic examples. My information:
Name: Glen Ovamir
Company: Ovamir Capital
Logo: OC
Address: 1470 N Thornwick Rd, Suite 210 | Harrowby, IL 60487
Phone: 555-210-0192
Email: glenovamir@ovamircap.com
Slogan: Building Strength Through Capital

Feel free to leave out any of the information above except my name.

I have selected Double-sided, but I am also open to Single-sided

Target Market(s)

22-70. income greater than 150k/year

Industry/Entity Type

Finance

Contact Information for Business Card

See Project Description

Requirements
Must have
• Ivory or "antiqued" background similar to the reference pictures

```html
<!DOCTYPE html>
<html lang="en">
<head>
<meta charset="utf-8">
<title>Ovamir Capital — Business Card</title>
<link rel="stylesheet" href="https://fonts.googleapis.com/css2?family=Old+Standard+TT:wght@400;700&display=swap">
<style>
  :root {
    --backdrop: #4a2c1a;
    --paper-light: #fbf7ea;
    --paper-mid: #f1e6c9;
    --paper-edge: #d9c597;
    --ink: #1f1c19;
    --rule: #3a342c;
  }
  * { margin: 0; padding: 0; box-sizing: border-box; }
  html, body {
    width: 1200px; height: 1000px; overflow: hidden;
    background: var(--backdrop);
  }
  .canvas {
    position: relative; width: 1200px; height: 1000px;
    font-family: "Old Standard TT", Georgia, serif;
    color: var(--ink);
  }
  .card {
    position: absolute;
    background: radial-gradient(ellipse at 45% 45%, var(--paper-light) 0%, var(--paper-mid) 60%, var(--paper-edge) 100%);
    box-shadow: 0 10px 24px rgba(0,0,0,0.45);
    text-align: center;
  }
  .card-front { left: 180px; top: 140px; width: 640px; height: 360px; }
  .card-back  { left: 402px; top: 522px; width: 630px; height: 358px; }

  .monogram {
    position: absolute; left: 0; right: 0;
    display: flex; align-items: center; justify-content: center; gap: 10px;
    font-weight: 700; color: var(--ink);
  }
  .monogram-dot { border: 2px solid var(--ink); border-radius: 50%; }
  .card-front .monogram { top: 96px; font-size: 64px; letter-spacing: 4px; }
  .card-front .monogram-dot { width: 14px; height: 14px; }
  .card-back .monogram { top: 34px; font-size: 26px; letter-spacing: 2px; }
  .card-back .monogram-dot { width: 7px; height: 7px; border-width: 1.5px; }

  .company-name {
    position: absolute; left: 0; right: 0; top: 212px;
    font-size: 36px; letter-spacing: 2px; font-weight: 400;
  }
  .company-rule {
    position: absolute; left: 226px; width: 216px; top: 264px;
    height: 1px; background: var(--rule);
  }
  .slogan {
    position: absolute; left: 0; right: 0; top: 280px;
    font-size: 11px; letter-spacing: 3.5px; text-transform: uppercase;
  }

  .person-name {
    position: absolute; left: 0; right: 0; top: 122px;
    font-size: 29px; letter-spacing: 2.5px; text-transform: uppercase;
    font-weight: 400;
  }
  .address {
    position: absolute; left: 0; right: 0; top: 194px;
    font-size: 19px; line-height: 25px; letter-spacing: 1.5px; text-transform: uppercase;
  }
  .contact-row {
    position: absolute; left: 22px; right: 24px; bottom: 18px;
    display: flex; justify-content: space-between;
    font-size: 18px; letter-spacing: 0.6px;
  }
</style>
</head>
<body>
<main class="canvas">
  <section class="card card-front" aria-label="Card front">
    <div class="monogram"><span class="monogram-dot"></span><span>OC</span></div>
    <h1 class="company-name">OVAMIR CAPITAL</h1>
    <div class="company-rule"></div>
    <p class="slogan">Building Strength Through Capital</p>
  </section>

  <section class="card card-back" aria-label="Card back">
    <div class="monogram"><span class="monogram-dot"></span><span>OC</span></div>
    <h2 class="person-name">Glen Ovamir</h2>
    <p class="address">1470 N Thornwick Rd, Suite 210<br>Harrowby, IL 60487</p>
    <div class="contact-row">
      <span class="phone">555-210-0192</span>
      <span class="email">glenovamir@ovamircap.com</span>
    </div>
  </section>
</main>
</body>
</html>
```